hawkforge structural steel

8 1/2" x 11" flyer color both sides. Use at least 12 pictures.

Add the word; structural under HawkForge to logo

bullet points:
Laser Accuracy
On-time scheduling
Own our Equipment
39 Years Exp.
Manufacturing Construction Brackets Since 1982
We manufacture custom ibeams in Phoenix, AZ
Certified welders

Hawkforge Plant
2814 n. 17th avenue, suite-3
Phx, AZ 85019
480-629-8107

Target Market(s)

Architects, builders

Industry/Entity Type

construction

Colors
0054AA
0677BA
7BADD7
CADEEF
E8F1F8

```html
<!DOCTYPE html>
<html lang="en">
<head>
<meta charset="utf-8">
<title>HawkForge Structural Steel – Flyer</title>
<link rel="stylesheet" href="https://fonts.googleapis.com/css2?family=Poppins:wght@300;400;500;600;700;800&display=swap">
<style>
  :root{
    --steel-blue:#45608c;
    --steel-blue-light:#5b78a6;
    --ink:#1c2130;
    --ink-deep:#161a26;
    --paper:#ffffff;
    --backdrop:#eef0f4;
    --rule:#2a3145;
    --muted:#d9dee8;
  }
  *{margin:0;padding:0;box-sizing:border-box}
  html,body{width:1200px;height:2615px;overflow:hidden;background:var(--backdrop);font-family:"Poppins",sans-serif}
  .flyer{position:absolute;left:50px;top:607px;width:1100px;height:1400px;background:var(--paper);box-shadow:0 6px 24px rgba(0,0,0,.18);overflow:hidden}
  .brand-box{position:absolute;left:0;top:0;width:342px;height:215px;background:var(--paper);display:flex;flex-direction:column;align-items:center;justify-content:center;gap:6px}
  .brand-mark{display:flex;align-items:center;gap:10px}
  .brand-dot{width:22px;height:22px;border-radius:50%;background:var(--steel-blue)}
  .brand-name{font-size:34px;font-weight:600;color:var(--steel-blue);letter-spacing:.5px}
  .brand-sub{font-size:19px;font-weight:400;color:var(--steel-blue);letter-spacing:3px}
  .title-band{position:absolute;left:342px;top:0;width:758px;height:215px;background:var(--steel-blue);padding:22px 0 0 44px}
  .title-main{font-size:94px;font-weight:800;color:var(--ink);line-height:1;letter-spacing:-1px}
  .title-sub{font-size:62px;font-weight:400;color:var(--paper);line-height:1.15;letter-spacing:1px}
  .hero-photo{position:absolute;left:0;top:215px;width:629px;height:375px;background:linear-gradient(135deg,#3a4a6a 0%,#6b5a55 45%,#2a6a6a 70%,#1e2638 100%)}
  .hero-panel{position:absolute;left:629px;top:215px;width:471px;height:375px;background:linear-gradient(160deg,#23283a,var(--ink-deep));padding:82px 0 0 54px;color:var(--paper)}
  .hero-panel .l1{font-size:42px;font-weight:700;line-height:1.1}
  .hero-panel .l2{font-size:42px;font-weight:400;line-height:1.1}
  .hero-panel .l3{font-size:38px;font-weight:700;line-height:1.1}
  .since-tag{display:inline-block;margin-top:28px;background:var(--steel-blue);padding:4px 18px;font-size:25px;font-weight:300}
  .since-tag b{font-weight:500}
  .feature{position:absolute;left:52px;display:flex;align-items:center;gap:42px;transform:translateY(-50%)}
  .feature-icon{width:84px;height:84px;border-radius:50%;border:3px solid var(--steel-blue);display:flex;align-items:center;justify-content:center}
  .feature-label{font-size:29px;font-weight:600;color:var(--ink);letter-spacing:.3px}
  .feature-label span{color:var(--steel-blue)}
  .divider{position:absolute;left:52px;width:571px;border-top:3px dashed var(--ink)}
  .side-photo{position:absolute;left:658px;width:368px;border:2px solid var(--paper);outline:1px solid #c9ced8}
  .photo-forge{top:611px;height:231px;background:linear-gradient(180deg,#1c2c5a 0%,#2c3f7a 40%,#e0561c 62%,#1e2a4a 85%)}
  .photo-grinder{top:852px;height:230px;background:radial-gradient(circle at 40% 75%,#c07030 0%,#3a4660 28%,#1a2236 70%)}
  .photo-mill{top:1096px;height:228px;background:linear-gradient(160deg,#5a86b0 0%,#2a5a8a 45%,#1a3a6a 75%,#c8452a 100%);z-index:2}
  .info-band{position:absolute;left:0;top:1106px;width:1100px;height:252px;background:var(--ink)}
  .plant-title{position:absolute;left:52px;top:1142px;width:280px;font-size:27px;font-weight:600;color:var(--paper);padding-bottom:6px;border-bottom:2px solid var(--muted)}
  .plant-title span{font-weight:400}
  .plant-line{position:absolute;left:52px;display:flex;align-items:center;gap:18px;color:var(--paper);font-size:20px;line-height:1.25}
  .plant-line svg{flex:none}
  .years{position:absolute;left:371px;top:1130px;color:var(--paper)}
  .years-num{font-size:92px;font-weight:700;color:var(--steel-blue);line-height:1}
  .years-tag{position:absolute;left:108px;top:52px;background:var(--steel-blue);font-size:22px;font-weight:300;padding:0 10px;line-height:30px}
  .years-exp{position:absolute;left:0;top:100px;font-size:24px;font-weight:500;letter-spacing:7px;white-space:nowrap}
  .call{position:absolute;left:371px;top:1262px;display:flex;align-items:center;gap:10px;font-size:27px;font-weight:400;color:var(--steel-blue)}
  .call b{font-weight:600}
  .phone{position:absolute;left:371px;top:1294px;font-size:38px;font-weight:700;color:var(--paper);letter-spacing:1px}
</style>
</head>
<body>
<main class="flyer">
  <header>
    <div class="brand-box">
      <div class="brand-mark"><span class="brand-dot"></span><span class="brand-name">HAWKFORGE</span></div>
      <div class="brand-sub">STRUCTURAL</div>
    </div>
    <div class="title-band">
      <h1 class="title-main">HAWKFORGE</h1>
      <p class="title-sub">STRUCTURAL STEEL</p>
    </div>
  </header>

  <div class="hero-photo" role="img" aria-label="Worker in green jacket grinding a steel pipe with sparks flying"></div>
  <section class="hero-panel">
    <div class="l1">Manufacturing</div>
    <div class="l2">CONSTRUCTION</div>
    <div class="l3">BRACKETS</div>
    <div class="since-tag">SINCE <b>1982</b></div>
  </section>

  <section class="features">
    <div class="feature" style="top:666px">
      <div class="feature-icon"><svg width="44" height="44" viewBox="0 0 44 44" fill="none" stroke="#45608c" stroke-width="3"><rect x="12" y="4" width="20" height="8"/><path d="M22 12v14M16 30l6-4 6 4M6 38h32"/></svg></div>
      <div class="feature-label">LASER <span>ACCURACY</span></div>
    </div>
    <div class="divider" style="top:725px"></div>
    <div class="feature" style="top:780px">
      <div class="feature-icon"><svg width="44" height="44" viewBox="0 0 44 44" fill="none" stroke="#45608c" stroke-width="3"><rect x="5" y="9" width="30" height="26"/><path d="M5 16h30M12 5v7M28 5v7M11 22h4M18 22h4M25 22h4M11 28h4M18 28h4"/><circle cx="35" cy="35" r="5" fill="#fff"/></svg></div>
      <div class="feature-label">ON-TIME <span>SCHEDULING</span></div>
    </div>
    <div class="divider" style="top:839px"></div>
    <div class="feature" style="top:897px">
      <div class="feature-icon"><svg width="44" height="44" viewBox="0 0 44 44" fill="none" stroke="#45608c" stroke-width="3"><path d="M8 14l8-8 8 8M16 6v28"/><rect x="6" y="20" width="14" height="16"/><rect x="24" y="14" width="14" height="22"/><path d="M4 38h36"/></svg></div>
      <div class="feature-label">OWN OUR <span>EQUIPMENT</span></div>
    </div>
    <div class="divider" style="top:959px"></div>
    <div class="feature" style="top:1018px">
      <div class="feature-icon"><svg width="44" height="44" viewBox="0 0 44 44" fill="none" stroke="#45608c" stroke-width="3"><path d="M12 20a10 10 0 0 1 20 0v6H12z"/><path d="M15 20h14M10 40v-6a12 6 0 0 1 24 0v6"/></svg></div>
      <div class="feature-label">CERTIFIED <span>WELDERS</span></div>
    </div>
    <div class="divider" style="top:1079px"></div>
  </section>

  <div class="side-photo photo-forge" role="img" aria-label="Glowing orange steel beam in a rolling mill"></div>
  <div class="side-photo photo-grinder" role="img" aria-label="Worker cutting steel with an angle grinder in the dark"></div>

  <footer class="info-band"></footer>
  <div class="side-photo photo-mill" role="img" aria-label="Workers in blue overalls and hard hats guiding hot steel in a plant"></div>

  <h2 class="plant-title">Hawkforge <span>Plant</span></h2>
  <div class="plant-line" style="top:1208px">
    <svg width="30" height="30" viewBox="0 0 30 30" fill="none" stroke="#5b78a6" stroke-width="3"><circle cx="15" cy="15" r="6"/><path d="M15 2v5M15 23v5M2 15h5M23 15h5M6 6l3 3M21 21l3 3M6 24l3-3M21 9l3-3"/></svg>
    <span>We manufacture custom<br>ibeams in Phoenix, AZ</span>
  </div>
  <div class="plant-line" style="top:1306px">
    <svg width="30" height="34" viewBox="0 0 30 34" fill="#5b78a6"><path d="M15 1a11 11 0 0 0-11 11c0 8 11 21 11 21s11-13 11-21A11 11 0 0 0 15 1zm0 15a4 4 0 1 1 0-8 4 4 0 0 1 0 8z"/></svg>
    <span>2814 n. 17th avenue,<br>suite-3 Phx, AZ 85019</span>
  </div>

  <div class="years">
    <div class="years-num">39</div>
    <div class="years-tag">YEARS</div>
    <div class="years-exp">EXPERIENCE</div>
  </div>
  <div class="call">
    <svg width="28" height="28" viewBox="0 0 28 28"><rect width="28" height="28" rx="5" fill="#45608c"/><path d="M9 6l3 4-2 2c1 3 3 5 6 6l2-2 4 3-2 3c-7 0-13-6-13-13z" fill="#1c2130"/></svg>
    <span>CALL US <b>NOW</b></span>
  </div>
  <div class="phone">480-629-8107</div>
</main>
</body>
</html>
```